Cosmetic injections clinic needs a fresh looking business card

We need a business card using the supplied logo and color scheme to attract future clients to our clinic. It should be modern and fresh, eye catching and not too busy. Simple and to the point is best. I would like two sided designs with the front indicating address and contact information, and the back in full color with white logo and descriptive information also provided.
Target Market(s)
Clients looking for non surgical beauty enhancements.
Contact Information for Business Card
MeloraSkin
14, 618 Birchmont Way
St. Albert, Alberta
K2P 7W3
Phone: 587-412-6630
Email: info@meloraskin.com
Requirements
Must have
- -Logo supplied with the name and address of the clinic
- -Back of card in full color with white logo with A small line of text indicating both of the following: Anti aging consultants and cosmetic injectables
- Located inside the Voyager Wellness Group

```html
<!DOCTYPE html>
<html lang="en">
<head>
<meta charset="utf-8">
<title>MeloraSkin Business Card</title>
<link href="https://fonts.googleapis.com/css2?family=Montserrat:wght@400;500;600;700&display=swap" rel="stylesheet">
<style>
  :root {
    --bg: #3a3b3d;
    --pink: #de649c;
    --purple: #7a62ad;
    --teal: #17b3bd;
    --grey: #8d8d8f;
    --white: #ffffff;
  }
  * { margin: 0; padding: 0; box-sizing: border-box; }
  html, body { width: 1200px; height: 1000px; overflow: hidden; }
  body {
    background: var(--bg);
    font-family: "Montserrat", Arial, sans-serif;
    position: relative;
  }
  .card {
    position: absolute;
    left: 300px;
    width: 600px;
    height: 340px;
    border-radius: 30px;
    overflow: hidden;
  }
  .card-back { top: 90px; background: var(--pink); }
  .card-front { top: 520px; background: var(--white); }

  /* back side */
  .back-brand {
    position: absolute;
    left: 92px; top: 108px;
    display: flex; align-items: center; gap: 18px;
  }
  .brand-dot {
    width: 78px; height: 78px; border-radius: 50%;
    background: var(--white);
  }
  .back-name {
    color: var(--white);
    font-weight: 600;
    font-size: 54px;
    line-height: 1;
    letter-spacing: 0.5px;
  }
  .back-tagline {
    position: absolute;
    left: 96px; top: 214px;
    color: var(--white);
    font-size: 16px;
    font-weight: 500;
    letter-spacing: 0.3px;
  }

  /* front side */
  .front-shape { position: absolute; inset: 0; }
  .front-mark {
    position: absolute;
    left: 420px; top: 96px;
    width: 160px;
    text-align: center;
    color: var(--white);
    font-weight: 600;
    font-size: 22px;
  }
  .front-name {
    position: absolute;
    left: 48px; top: 26px;
    color: var(--purple);
    font-weight: 600;
    font-size: 38px;
    line-height: 1;
  }
  .front-tagline {
    position: absolute;
    left: 50px; top: 72px;
    width: 290px;
    color: var(--grey);
    font-size: 12.5px;
    line-height: 1.35;
  }
  .front-tagline .network { color: var(--pink); font-weight: 500; }

  .contact-rail {
    position: absolute;
    left: 64px; top: 136px;
    width: 3px; height: 100px;
    background: var(--pink);
  }
  .contact-row {
    position: absolute;
    left: 48px;
    display: flex; align-items: flex-start; gap: 16px;
  }
  .contact-icon {
    width: 34px; height: 34px; border-radius: 50%;
    background: var(--pink);
    display: flex; align-items: center; justify-content: center;
    flex-shrink: 0;
  }
  .contact-text {
    color: var(--grey);
    font-size: 15px;
    line-height: 1.3;
    padding-top: 7px;
  }
  .contact-text .highlight { color: var(--pink); }
  .row-phone { top: 118px; }
  .row-email { top: 168px; }
  .row-address { top: 218px; }
</style>
</head>
<body>

  <section class="card card-back">
    <div class="back-brand">
      <div class="brand-dot"></div>
      <div class="back-name">MeloraSkin</div>
    </div>
    <p class="back-tagline">Anti Aging Consultants &amp; Cosmetic Injectables</p>
  </section>

  <section class="card card-front">
    <svg class="front-shape" viewBox="0 0 600 340" width="600" height="340">
      <polygon points="380,0 392,0 346,242 334,240" fill="var(--teal)"/>
      <polygon points="346,242 600,272 600,281 346,250" fill="var(--purple)"/>
      <polygon points="392,0 600,0 600,272 346,242" fill="var(--pink)"/>
    </svg>
    <div class="front-mark">MeloraSkin</div>

    <h1 class="front-name">MeloraSkin</h1>
    <p class="front-tagline">
      Anti Aging Consultants &amp; Cosmetic Injectables<br>
      Located inside the <span class="network">Voyager Wellness Group</span>
    </p>

    <div class="contact-rail"></div>

    <div class="contact-row row-phone">
      <span class="contact-icon">
        <svg width="18" height="18" viewBox="0 0 24 24"><path fill="#fff" d="M6.6 10.8a15.1 15.1 0 0 0 6.6 6.6l2.2-2.2a1 1 0 0 1 1-.25 11.4 11.4 0 0 0 3.6.57 1 1 0 0 1 1 1V20a1 1 0 0 1-1 1A17 17 0 0 1 3 4a1 1 0 0 1 1-1h3.5a1 1 0 0 1 1 1c0 1.25.2 2.45.57 3.57a1 1 0 0 1-.25 1z"/></svg>
      </span>
      <span class="contact-text">587-412-6630</span>
    </div>

    <div class="contact-row row-email">
      <span class="contact-icon">
        <svg width="18" height="18" viewBox="0 0 24 24" fill="none" stroke="#fff" stroke-width="1.8"><circle cx="12" cy="12" r="9"/><ellipse cx="12" cy="12" rx="4" ry="9"/><line x1="3" y1="12" x2="21" y2="12"/></svg>
      </span>
      <span class="contact-text">info@<span class="highlight">meloraskin</span>.com</span>
    </div>

    <div class="contact-row row-address">
      <span class="contact-icon">
        <svg width="16" height="18" viewBox="0 0 24 24"><path fill="#fff" d="M12 2a7 7 0 0 0-7 7c0 5.2 7 13 7 13s7-7.8 7-13a7 7 0 0 0-7-7zm0 9.5A2.5 2.5 0 1 1 12 6.5a2.5 2.5 0 0 1 0 5z"/></svg>
      </span>
      <span class="contact-text">
        <span class="highlight">MeloraSkin</span><br>
        14, 618 Birchmont Way<br>
        St. Albert, Alberta<br>
        K2P 7W3
      </span>
    </div>
  </section>

</body>
</html>
```